Door Hanger General Contractor

design high quality marketing piece to promote our general contractor business.
Use all content create badges, banners, bubbles, boxes ect to highlight text.
Template format is uploaded in images
Make font as large as possible, minimize negative space, fill areas
FRONT SIDE
Your Neighbor Just Remodeled
Come See Our Work at:
(under this create blank white box placeholder for address)
LOVE YOUR HOME AGAIN!
WE MAKE REMODELING EASY
FREE 3D DESIGN SERVICES
FREE ESTIMATES
LICENSED GENERAL CONTRACTORS
We Specialize in:
Kitchen Remodel
Bathroom Remodel
Interior/Exterior Painting
Flooring: Carpet, Vinyl, Wood & Tile
Energy Efficient Upgrades
Window/Door Replacement
WATER & MOLD DAMAGE
BACK SIDE
GET STARTED IN 3 SIMPLE STEPS:
1 ORDER FREE ESTIMATE & DESIGN
2 APPROVE ESTIMATE & DESIGN
3 HEARTHWAY RENOVATORS BUILDS YOUR DREAM
Thinking About Selling?
We Buy Homes
GET CASH OFFER
SELLING MADE EASY
CALL NOW!!
Hearthway Renovators Inc.
858-555-0174 Call/Text
BrightGableHomes.example
CSLB# 4087261
home owners
General Contractor

```html
<!DOCTYPE html>
<html lang="en">
<head>
<meta charset="utf-8">
<title>Hearthway Renovators Door Hanger</title>
<link rel="stylesheet" href="https://fonts.googleapis.com/css2?family=Oswald:wght@400;500;600;700&display=swap">
<style>
  :root {
    --page: #dcdcdd;
    --blue: #2a68c0;
    --blue-deep: #1f56a8;
    --blue-bright: #2f86d6;
    --white: #ffffff;
    --ink-blue: #1f5fb6;
    --photo-kitchen: #cfc6bb;
    --photo-kitchen-2: #8d7763;
    --photo-bath: #e6e9ea;
    --photo-bath-2: #b9cfcf;
    --photo-street: #7c9a6a;
    --photo-sign: #e0a33a;
    --badge: #2b2b2b;
  }
  * { box-sizing: border-box; margin: 0; padding: 0; }
  html, body { width: 1200px; height: 1200px; overflow: hidden; }
  body {
    background: var(--page);
    font-family: "Oswald", "Arial Narrow", sans-serif;
    position: relative;
  }
  .card {
    position: absolute;
    top: 100px;
    width: 500px;
    height: 1000px;
    overflow: hidden;
    box-shadow: 0 10px 24px rgba(0,0,0,0.18);
  }
  .card--front { left: 70px; }
  .card--back { left: 630px; }
  .card svg.shapes { position: absolute; inset: 0; width: 500px; height: 1000px; }
  .abs { position: absolute; }
  .upper { text-transform: uppercase; }

  /* front */
  .brand {
    top: 26px; right: 28px;
    display: flex; align-items: center; gap: 8px;
    color: var(--white); font-weight: 400; font-size: 14px; letter-spacing: 1.5px;
  }
  .brand__mark { width: 14px; height: 14px; border: 1.5px solid var(--white); }
  .headline {
    top: 78px; left: 28px;
    color: var(--white); font-weight: 700; font-size: 38px; line-height: 44px;
  }
  .love {
    top: 560px; left: 28px;
    color: var(--blue-bright); font-weight: 700; font-size: 40px; line-height: 1;
  }
  .perks {
    top: 612px; left: 30px; list-style: none;
    color: var(--blue-bright); font-weight: 600; font-size: 19px; line-height: 24px;
  }
  .perks li::before, .services li::before, .sell-list li::before {
    content: ""; display: inline-block; width: 7px; height: 7px; border-radius: 50%;
    margin-right: 10px; vertical-align: middle; background: currentColor;
  }
  .licensed {
    top: 710px; left: 28px;
    color: var(--white); font-weight: 700; font-size: 27px; line-height: 1;
  }
  .specialize {
    top: 746px; left: 28px;
    color: var(--white); font-weight: 600; font-size: 18px; line-height: 24px;
  }
  .services {
    top: 776px; list-style: none;
    color: var(--white); font-weight: 500; font-size: 15px; line-height: 19px;
  }
  .services--a { left: 40px; width: 205px; }
  .services--b { left: 258px; width: 218px; }
  .services li { margin-bottom: 3px; padding-left: 17px; text-indent: -17px; }
  .address-box {
    top: 929px; left: 254px; width: 222px; height: 28px;
    background: var(--blue); color: var(--white);
    font-size: 13px; font-weight: 400; display: flex; align-items: center; padding-left: 12px;
  }
  .neighbor {
    top: 904px; left: 28px;
    color: var(--ink-blue); font-weight: 700; font-size: 21px; line-height: 26px;
  }

  /* back */
  .steps-title {
    top: 36px; left: 28px;
    color: var(--white); font-weight: 700; font-size: 31px; line-height: 1;
  }
  .steps { top: 92px; left: 28px; list-style: none; color: var(--white); }
  .steps li {
    display: flex; gap: 12px; align-items: flex-start;
    font-weight: 500; font-size: 19px; line-height: 23px; margin-bottom: 12px;
  }
  .steps__num {
    flex: none; width: 22px; height: 22px; border-radius: 50%;
    background: var(--white); color: var(--blue);
    font-size: 13px; font-weight: 700; display: flex; align-items: center; justify-content: center;
  }
  .sell-ribbon {
    top: 778px; left: 18px; padding: 6px 16px;
    background: var(--blue); color: var(--white);
    font-weight: 700; font-size: 24px; line-height: 1;
  }
  .sell-list {
    top: 824px; left: 30px; list-style: none;
    color: var(--blue-bright); font-weight: 600; font-size: 20px; line-height: 26px;
  }
  .cash-offer {
    top: 640px; right: 26px;
    color: var(--blue-bright); font-weight: 700; font-size: 22px;
  }
  .badge { background: var(--badge); }
  .badge--shield { top: 686px; right: 40px; width: 52px; height: 58px; border-radius: 6px 6px 26px 26px; }
  .badge--square { top: 758px; right: 110px; width: 56px; height: 44px; }
  .badge--cert { top: 818px; right: 44px; width: 104px; height: 40px; }
  .badge--round { top: 818px; right: 162px; width: 44px; height: 40px; background: #b8c9a4; border-radius: 10px; }
  .call { top: 922px; left: 24px; color: var(--white); }
  .call__label { font-weight: 700; font-size: 24px; line-height: 1; }
  .contact-line {
    display: flex; align-items: center; gap: 7px;
    font-weight: 500; font-size: 15px; margin-top: 6px;
  }
  .contact-line svg { width: 14px; height: 14px; flex: none; }
  .company {
    top: 908px; right: 24px; text-align: right; color: var(--white);
  }
  .company__name { font-weight: 700; font-size: 22px; line-height: 1; }
  .company__web { font-size: 14px; font-weight: 400; margin-top: 6px; display: flex; gap: 6px; align-items: center; justify-content: flex-end; }
  .company__license { font-size: 14px; font-weight: 500; margin-top: 4px; }
</style>
</head>
<body>

<section class="card card--front" aria-label="Door hanger front">
  <svg class="shapes" viewBox="0 0 500 1000" aria-hidden="true">
    <defs>
      <linearGradient id="kitchenTone" x1="0" y1="0" x2="1" y2="1">
        <stop offset="0" stop-color="var(--photo-kitchen)"/>
        <stop offset="1" stop-color="var(--photo-kitchen-2)"/>
      </linearGradient>
    </defs>
    <rect width="500" height="1000" fill="var(--white)"/>
    <polygon points="0,0 500,0 500,230 0,380" fill="var(--blue)"/>
    <polygon points="0,386 500,236 500,410 0,548" fill="url(#kitchenTone)"/>
    <polygon points="0,702 330,702 356,680 500,680 500,892 0,892" fill="var(--blue)"/>
    <rect x="0" y="972" width="500" height="28" fill="var(--blue-bright)"/>
  </svg>
  <div class="abs" role="img" aria-label="Photo of a bright remodeled kitchen with island and pendant lights" style="top:300px;left:0;width:500px;height:200px;"></div>
  <div class="abs" role="img" aria-label="Kitchen design sketch blending into a finished render" style="top:440px;right:24px;width:150px;height:100px;background:linear-gradient(135deg,#f0e6cf,#d9a94a);"></div>

  <div class="abs brand upper"><span class="brand__mark"></span>Hearthway Renovators</div>
  <h1 class="abs headline upper">We make<br>remodeling easy free<br>3D design services free<br>estimates</h1>

  <h2 class="abs love upper">Love your home again!</h2>
  <ul class="abs perks upper">
    <li>We make remodeling easy</li>
    <li>Free 3D design services</li>
    <li>Free estimates</li>
  </ul>

  <h2 class="abs licensed upper">Licensed general contractors</h2>
  <p class="abs specialize">We Specialize in:</p>
  <ul class="abs services services--a">
    <li>Kitchen Remodel</li>
    <li>Interior/Exterior Painting</li>
    <li>Energy Efficient Upgrades</li>
  </ul>
  <ul class="abs services services--b">
    <li>WATER &amp; MOLD DAMAGE</li>
    <li>Flooring: Carpet, Vinyl, Wood &amp; Tile</li>
    <li>Window/Door Replacement</li>
    <li>Bathroom Remodel</li>
  </ul>

  <p class="abs neighbor">Your Neighbor Just Remodeled<br>Come See Our Work at:</p>
  <div class="abs address-box">Address your street, Road 123</div>
</section>

<section class="card card--back" aria-label="Door hanger back">
  <svg class="shapes" viewBox="0 0 500 1000" aria-hidden="true">
    <defs>
      <linearGradient id="bathTone" x1="0" y1="0" x2="1" y2="1">
        <stop offset="0" stop-color="var(--photo-bath)"/>
        <stop offset="1" stop-color="var(--photo-bath-2)"/>
      </linearGradient>
      <linearGradient id="streetTone" x1="0" y1="0" x2="1" y2="1">
        <stop offset="0" stop-color="var(--photo-street)"/>
        <stop offset="1" stop-color="#5b86c4"/>
      </linearGradient>
      <linearGradient id="signTone" x1="0" y1="0" x2="1" y2="1">
        <stop offset="0" stop-color="#d8dcd8"/>
        <stop offset="1" stop-color="var(--photo-sign)"/>
      </linearGradient>
    </defs>
    <rect width="500" height="1000" fill="var(--white)"/>
    <polygon points="0,0 500,0 500,190 0,340" fill="var(--blue)"/>
    <polygon points="0,346 500,196 500,466 0,616" fill="url(#bathTone)"/>
    <polygon points="0,622 226,554 226,694 0,762" fill="url(#streetTone)"/>
    <polygon points="234,552 500,472 500,614 234,692" fill="url(#signTone)"/>
    <polygon points="0,922 500,878 500,1000 0,1000" fill="var(--blue)"/>
    <polygon points="0,912 500,868 500,872 0,916" fill="var(--blue)"/>
  </svg>
  <div class="abs" role="img" aria-label="Photo of a white bathroom with glass shower and brass fixtures" style="top:260px;left:0;width:500px;height:300px;"></div>
  <div class="abs" role="img" aria-label="Photo of a homeowner reviewing an offer outside a house" style="top:600px;left:0;width:226px;height:130px;"></div>
  <div class="abs" role="img" aria-label="Photo of a for sale sign marked sold over asking" style="top:540px;left:234px;width:266px;height:120px;"></div>

  <h2 class="abs steps-title upper">Get started in 3 simple steps:</h2>
  <ol class="abs steps upper">
    <li><span class="steps__num">1</span><span>Order free estimate &amp; design</span></li>
    <li><span class="steps__num">2</span><span>Approve estimate &amp; design</span></li>
    <li><span class="steps__num">3</span><span>Hearthway Renovators builds<br>your dream</span></li>
  </ol>

  <p class="abs cash-offer upper">• Get cash offer</p>
  <div class="abs badge badge--shield" aria-hidden="true"></div>
  <div class="abs badge badge--square" aria-hidden="true"></div>
  <div class="abs badge badge--cert" aria-hidden="true"></div>
  <div class="abs badge badge--round" aria-hidden="true"></div>

  <h2 class="abs sell-ribbon upper">Thinking about selling?</h2>
  <ul class="abs sell-list upper">
    <li>We buy homes</li>
    <li>Selling made easy</li>
  </ul>

  <div class="abs call">
    <p class="call__label upper">Call now/text</p>
    <p class="contact-line">
      <svg viewBox="0 0 24 24" aria-hidden="true"><circle cx="12" cy="12" r="12" fill="#fff"/><path d="M8 6l2 0 1 3-1.5 1a8 8 0 0 0 4 4l1-1.5 3 1 0 2c-5 1-10-4-9.5-9.5z" fill="#2a68c0"/></svg>
      858-555-0174
    </p>
  </div>
  <div class="abs company">
    <p class="company__name upper">Hearthway Renovators Inc.</p>
    <p class="company__web">
      <svg viewBox="0 0 24 24" width="13" height="13" aria-hidden="true"><circle cx="12" cy="12" r="10" fill="none" stroke="#fff" stroke-width="2"/><path d="M2 12h20M12 2c4 4 4 16 0 20M12 2c-4 4-4 16 0 20" fill="none" stroke="#fff" stroke-width="1.6"/></svg>
      BrightGableHomes.example
    </p>
    <p class="company__license">CSLB# 4087261</p>
  </div>
</section>

</body>
</html>
```